Ironvale Holdings Business card

We need a an amazing matte black and gold card! W are a finance investing company so we want something that's eye catching and sleek. We want it to be attractive and sleek and represent money. Heck with would like the letters and lgo to be printed as 24k gold one day. We have the logo added so please use the color scheme with the logo and have that beautifully placed on one side.

Target Market(s)

Investors of all ages

Industry/Entity Type

Financial

Contact Information for Business Card

Black and matte with gold lettering follow logo colrs please.

Font styles to use
Other font styles liked:
• you decide

Colors

Designer to choose colors to be used in the design.

Requirements
Must have
• Matte Black and Gold, logo on one side. job title and name , website, phone number and email address on the other side
Nice to have
• Matte black and crisp finish to attract investors
Should not have
• playful, very professional!

```html
<!DOCTYPE html>
<html lang="en">
<head>
<meta charset="utf-8">
<title>Ironvale Holdings Business Card</title>
<link href="https://fonts.googleapis.com/css2?family=Tinos:wght@400;700&display=swap" rel="stylesheet">
<style>
  :root {
    --backdrop: #262626;
    --card-black: #050505;
    --gold: #d4ae3c;
    --white: #f2f2f2;
    --card-w: 620px;
    --card-h: 354px;
  }
  * { margin: 0; padding: 0; box-sizing: border-box; }
  html, body {
    width: 1200px;
    height: 880px;
    overflow: hidden;
    background: var(--backdrop);
    font-family: "Tinos", "Times New Roman", serif;
  }
  .stage {
    position: relative;
    width: 1200px;
    height: 880px;
  }
  .card {
    position: absolute;
    width: var(--card-w);
    height: var(--card-h);
    background: var(--card-black);
    border-radius: 18px;
    box-shadow: 0 14px 30px rgba(0, 0, 0, 0.45);
    overflow: hidden;
  }
  .card--front { left: 290px; top: 60px; }
  .card--back  { left: 290px; top: 466px; }

  /* Front */
  .front-brand {
    position: absolute;
    inset: 0;
    display: flex;
    align-items: center;
    justify-content: center;
  }
  .brand-name {
    color: var(--gold);
    font-weight: 400;
    font-size: 44px;
    letter-spacing: 1px;
    text-transform: uppercase;
    white-space: nowrap;
  }

  /* Back */
  .back-brand {
    position: absolute;
    left: 62px;
    top: 0;
    bottom: 0;
    display: flex;
    align-items: center;
  }
  .back-brand .brand-name {
    font-size: 26px;
    letter-spacing: 0.5px;
    writing-mode: vertical-rl;
    transform: rotate(180deg);
  }
  .details {
    position: absolute;
    left: 200px;
    top: 62px;
    color: var(--white);
  }
  .person-name {
    color: var(--gold);
    font-weight: 700;
    font-size: 22px;
    letter-spacing: 0.5px;
    text-transform: uppercase;
    white-space: nowrap;
  }
  .person-title {
    font-size: 17px;
    margin-top: 2px;
  }
  .rule {
    width: 190px;
    height: 3px;
    background: var(--white);
    margin: 14px 0 12px;
  }
  .rule--short { margin-left: 90px; margin-top: 12px; }
  .contact-list { list-style: none; }
  .contact-item {
    display: flex;
    align-items: center;
    gap: 10px;
    font-size: 16px;
    line-height: 1;
    margin-bottom: 7px;
    white-space: nowrap;
  }
  .contact-icon {
    width: 20px;
    height: 20px;
    flex: none;
  }
  .address {
    font-size: 16px;
    line-height: 1.3;
    margin-left: 90px;
    white-space: nowrap;
  }
</style>
</head>
<body>
<main class="stage">

  <section class="card card--front" aria-label="Card front">
    <div class="front-brand">
      <span class="brand-name">Ironvale Holdings</span>
    </div>
  </section>

  <section class="card card--back" aria-label="Card back">
    <div class="back-brand">
      <span class="brand-name">Ironvale Holdings</span>
    </div>

    <div class="details">
      <p class="person-name">Marcus Hale</p>
      <p class="person-title">CEO</p>
      <div class="rule"></div>

      <ul class="contact-list">
        <li class="contact-item">
          <svg class="contact-icon" viewBox="0 0 20 20" aria-hidden="true">
            <circle cx="10" cy="10" r="9.5" fill="var(--gold)"/>
            <rect x="7" y="4.5" width="6" height="11" rx="1.2" fill="none" stroke="#050505" stroke-width="1.4"/>
            <line x1="9" y1="13.5" x2="11" y2="13.5" stroke="#050505" stroke-width="1.2"/>
          </svg>
          <span>555 010 2030</span>
        </li>
        <li class="contact-item">
          <svg class="contact-icon" viewBox="0 0 20 20" aria-hidden="true">
            <circle cx="10" cy="10" r="9.5" fill="var(--gold)"/>
            <rect x="5" y="6.5" width="10" height="7" fill="none" stroke="#050505" stroke-width="1.3"/>
            <polyline points="5,6.5 10,10.8 15,6.5" fill="none" stroke="#050505" stroke-width="1.3"/>
          </svg>
          <span>contact@ironvaleholdings.com</span>
        </li>
        <li class="contact-item">
          <svg class="contact-icon" viewBox="0 0 20 20" aria-hidden="true">
            <circle cx="10" cy="10" r="9.5" fill="var(--gold)"/>
            <circle cx="10" cy="10" r="5" fill="none" stroke="#050505" stroke-width="1.2"/>
            <ellipse cx="10" cy="10" rx="2.2" ry="5" fill="none" stroke="#050505" stroke-width="1"/>
            <line x1="5" y1="10" x2="15" y2="10" stroke="#050505" stroke-width="1"/>
          </svg>
          <span>www.IRONVALEHOLDINGS.com</span>
        </li>
      </ul>

      <div class="rule rule--short"></div>
      <p class="address">PO BOX 480, Harbour Lane<br>9th street, Geelong</p>
    </div>
  </section>

</main>
</body>
</html>
```